Online Consultancy Needs a New Logo & Business Card Design

Based on the new logo we just received from another contest here on Drawnest,

You'll find a few different versions of our logo as well as examples of business card designs we like in this folder:
==> https://files.velmorashare.net/view?id=7Kp2QwTx9LmRvZ4nHs8YbC1uF3aE&mode=open

We are considering two options:
- clean, black design
- clean, white/blue design

We're willing to consider both options.

We're considering adding some special effects to the cards when printing - emboss, rounded corners, etc.

However, please deliver a design WITHOUT round corners.

Target Market(s)

Successful business people, serious and older audience.

Industry/Entity Type

Business

Contact Information for Business Card

For the business card, I would like a minimalistic card with the logo on one side (perhaps in the middle) and the contact information on the other.

For the contact information please use:
Name: Peter Lang
Position: Founder
Email: peter.lang@morvel.com
Phone Number: +381 64 70 81 925
Website URL: www.morvel.com

Font styles to use
Serif
Sans Serif

Requirements
Must have
• Must fit in perfectly with our current website design.

```html
<!DOCTYPE html>
<html lang="en">
<head>
<meta charset="utf-8">
<title>Morvel Business Card</title>
<link rel="stylesheet" href="https://fonts.googleapis.com/css2?family=Exo+2:wght@400;600&family=Oswald:wght@400;500&display=swap">
<style>
  :root {
    --page-bg: #d9d9d9;
    --card-dark: #333333;
    --silver-light: #f4f4f4;
    --silver-mid: #c9c9c9;
    --ink: #3a3a3a;
    --ink-soft: #555555;
    --white: #ffffff;
  }
  * { margin: 0; padding: 0; box-sizing: border-box; }
  html, body { width: 1200px; height: 933px; overflow: hidden; }
  body {
    background: var(--page-bg);
    font-family: "Exo 2", Arial, sans-serif;
    position: relative;
  }
  .card {
    position: absolute;
    left: 300px;
    width: 600px;
    height: 343px;
    box-shadow: 0 10px 28px rgba(0,0,0,0.22);
    overflow: hidden;
  }
  .card-back { top: 83px; background: var(--card-dark); }
  .card-front { top: 506px; }
  .card-art { position: absolute; inset: 0; width: 100%; height: 100%; }

  .brand {
    position: absolute;
    display: flex;
    align-items: center;
    gap: 12px;
    color: var(--white);
    font-family: "Exo 2", Arial, sans-serif;
    font-weight: 600;
    letter-spacing: 1px;
  }
  .brand-dot { border-radius: 50%; background: var(--white); }
  .card-back .brand { left: 50%; top: 50%; transform: translate(-50%, -50%); font-size: 54px; }
  .card-back .brand-dot { width: 22px; height: 22px; }
  .card-front .brand { left: 70px; top: 84px; font-size: 50px; }
  .card-front .brand-dot { width: 20px; height: 20px; }

  .person {
    position: absolute;
    right: 30px;
    top: 86px;
    text-align: right;
    color: var(--ink);
  }
  .person-name {
    font-family: "Oswald", Arial, sans-serif;
    font-weight: 500;
    font-size: 30px;
    letter-spacing: 1.5px;
    line-height: 1;
  }
  .person-role {
    font-family: "Exo 2", Arial, sans-serif;
    font-size: 11px;
    letter-spacing: 2.5px;
    margin-top: 6px;
    color: var(--ink-soft);
  }

  .contact-list {
    position: absolute;
    right: 22px;
    top: 226px;
    list-style: none;
    color: var(--ink);
    font-size: 12.5px;
    letter-spacing: 0.6px;
  }
  .contact-item {
    display: flex;
    justify-content: flex-end;
    align-items: center;
    gap: 8px;
    height: 21px;
  }
  .contact-icon {
    width: 15px; height: 15px;
    border-radius: 50%;
    background: var(--ink);
    display: flex; align-items: center; justify-content: center;
  }
  .contact-icon svg { width: 9px; height: 9px; fill: var(--white); }
</style>
</head>
<body>

<section class="card card-back" aria-label="Card back">
  <div class="brand"><span class="brand-dot"></span>morvel</div>
</section>

<section class="card card-front" aria-label="Card front">
  <svg class="card-art" viewBox="0 0 600 343" preserveAspectRatio="none" aria-hidden="true">
    <defs>
      <linearGradient id="silver-top" x1="0" y1="0" x2="1" y2="1">
        <stop offset="0" stop-color="#cfcfcf"/>
        <stop offset="0.5" stop-color="#f6f6f6"/>
        <stop offset="1" stop-color="#dcdcdc"/>
      </linearGradient>
      <linearGradient id="silver-bottom" x1="0" y1="0" x2="1" y2="0">
        <stop offset="0" stop-color="#bdbdbd"/>
        <stop offset="0.45" stop-color="#f2f2f2"/>
        <stop offset="1" stop-color="#e4e4e4"/>
      </linearGradient>
    </defs>
    <rect width="600" height="343" fill="url(#silver-bottom)"/>
    <polygon points="130,0 600,0 600,210" fill="url(#silver-top)"/>
    <polygon points="0,0 130,0 600,210 600,218 0,292" fill="var(--card-dark)"/>
    <polyline points="130,0 600,210" stroke="#9a9a9a" stroke-width="2" fill="none"/>
    <polyline points="600,218 0,292" stroke="#a8a8a8" stroke-width="3" fill="none"/>
    <polyline points="600,222 0,300" stroke="#ffffff" stroke-width="1.5" fill="none" opacity="0.8"/>
  </svg>

  <div class="brand"><span class="brand-dot"></span>morvel</div>

  <div class="person">
    <p class="person-name">PETER LANG</p>
    <p class="person-role">GENERAL MANAGER</p>
  </div>

  <ul class="contact-list">
    <li class="contact-item">+381 64 70 81 925
      <span class="contact-icon"><svg viewBox="0 0 10 10"><path d="M2 0.5h2l0.8 2.2-1.2 0.9a5 5 0 0 0 2.8 2.8l0.9-1.2 2.2 0.8v2A1 1 0 0 1 8.5 9 8 8 0 0 1 1 1.5a1 1 0 0 1 1-1z"/></svg></span>
    </li>
    <li class="contact-item">+381 64 70 81 925
      <span class="contact-icon"><svg viewBox="0 0 10 10"><rect x="2.5" y="0.5" width="5" height="9" rx="1"/></svg></span>
    </li>
    <li class="contact-item">peter.lang@morvel.com
      <span class="contact-icon"><svg viewBox="0 0 10 10"><path d="M0.5 2h9v6h-9z M0.5 2l4.5 3.5 4.5-3.5" stroke="#333" stroke-width="0.6"/></svg></span>
    </li>
    <li class="contact-item">www.morvel.com
      <span class="contact-icon"><svg viewBox="0 0 10 10"><circle cx="5" cy="5" r="4.2"/></svg></span>
    </li>
    <li class="contact-item">12 Kestrel Lane, 4th Floor, Novara
      <span class="contact-icon"><svg viewBox="0 0 10 10"><path d="M5 0.5a3.2 3.2 0 0 1 3.2 3.2C8.2 6 5 9.5 5 9.5S1.8 6 1.8 3.7A3.2 3.2 0 0 1 5 0.5z"/></svg></span>
    </li>
  </ul>
</section>

</body>
</html>
```